The website is called gearloftic.net. It's a DIY projects ( only mechanical engineering related projects ) where mechanical engineers/student can share their ideas/ DIY projects/tutorial/course projects/Graduation projects...etc.
The website is more or less like craftivora.net ( please spend some time in this website ), but strictly to mechanical engineer and it will feature projects like pumps, turbines, compressor, gearboxes, automotive ...etc
There will be four categories:
1- Create, it's where the user can share his project, so it will have a writing feature ( title, body , upload image at different locations of the body ...etc)
2- Tutorials, where is user can share a tutorial so it should have a writing feature also
3- Build, where the user can see others projects
4- Buy, two items: a- T-shirts, b-Books ( DIY books made by us )
Notes:
-In the Share and tutorial categories, the user should select subcategory ( Will give them to you later ).
-When clicking to "make" category the user can see all the posted projects, then he can select a sub category ( see partspindle.net )
- each user will have a personal page
- Buy category will be added later if the website succeeded
- landing page feature the latest projects,tutorial
This is the full detail about the website, if there is something specific please let me know.
*No logo is been made yet.
thanks.
Industry/Entity Type
Mechanical Engineering
Look and feel

```html
<!DOCTYPE html>
<html lang="en">
<head>
<meta charset="utf-8">
<title>Gearloftic — mechanical engineering related projects</title>
<link rel="stylesheet" href="https://fonts.googleapis.com/css2?family=Oswald:wght@500;600&family=Source+Sans+3:wght@400;600&family=Open+Sans:wght@400;600&display=swap">
<style>
:root{
  --page:#e9e9e9;
  --card:#ffffff;
  --card-line:#d4d4d4;
  --red:#c8321a;
  --ink:#3a3a3a;
  --ink-soft:#555;
  --muted:#8a8a8a;
  --pill:#c9c9c9;
  --pill-dark:#b5b5b5;
  --green:#7cbb1e;
  --footer:#2c2c2c;
  --footer-deep:#1f1f1f;
  --footer-text:#c9c9c9;
  --footer-faint:#6f6f6f;
}
*{box-sizing:border-box;margin:0;padding:0}
html,body{width:962px;height:1200px;overflow:hidden;background:var(--page)}
body{font-family:"Source Sans 3",sans-serif;color:var(--ink)}
.stage{position:relative;width:900px;height:1123px;transform:scale(1.0689);transform-origin:0 0}
.abs{position:absolute}
.heading{font-family:"Oswald",sans-serif;font-weight:600;font-size:17px;letter-spacing:-.2px;color:var(--ink);text-transform:uppercase;line-height:1}
.heading .accent{color:var(--red)}

/* top bar */
.top-pill{top:13px;height:16px;border-radius:8px;background:var(--pill);font-family:"Oswald",sans-serif;font-weight:500;font-size:13px;text-align:center;line-height:16px;color:var(--ink)}
.top-pill .accent{color:var(--red)}
.search{left:602px;top:9px;width:157px;height:21px;border-radius:11px;background:var(--pill)}
.search-field{position:absolute;left:10px;top:3px;width:75px;height:14px;background:#f4f4f4;border:1px solid #bbb;font-size:7px;color:#666;padding:2px 4px;line-height:9px}
.search-go{position:absolute;left:88px;top:3px;width:19px;height:14px;background:#eee;border:1px solid #bbb;font-size:7px;text-align:center;line-height:12px;color:#444}

/* header */
.masthead{left:142px;top:38px;width:611px;height:56px;background:linear-gradient(#f7f7f7,#dcdcdc);border:1px solid #c6c6c6;border-radius:3px;box-shadow:0 1px 2px rgba(0,0,0,.15)}
.brand-mark{position:absolute;left:46px;top:10px;width:34px;height:34px;border-radius:50%;background:#bdbdbd}
.brand-name{position:absolute;left:94px;top:9px;font-family:"Oswald",sans-serif;font-weight:600;font-size:22px;color:var(--ink-soft);letter-spacing:.3px;line-height:1}
.brand-tag{position:absolute;left:94px;top:36px;font-size:11.5px;color:var(--muted);line-height:1}
.main-nav{position:absolute;left:320px;top:17px;width:289px;height:22px;border-radius:6px;background:linear-gradient(#fafafa,#e3e3e3);border:1px solid #c2c2c2;display:flex;align-items:center;padding-left:6px}
.main-nav a{font-size:12.5px;color:var(--ink);text-decoration:none;padding:0 10px;border-left:1px solid #cfcfcf;line-height:14px}
.main-nav a:first-child{border-left:0}
.main-nav a.current{background:#dedede;line-height:20px}

/* call to action */
.submit-label{left:385px;top:116px;font-family:"Oswald",sans-serif;font-weight:600;font-size:20px;color:var(--red);letter-spacing:-.3px;line-height:1}
.make-pill{left:633px;top:112px;width:110px;height:38px;border-radius:12px;background:var(--pill);font-family:"Oswald",sans-serif;font-weight:600;font-size:27px;line-height:38px;text-align:center;color:#444}

/* slider */
.slider{left:144px;top:159px;width:617px;height:224px;background:var(--card);border:1px solid var(--card-line);border-radius:4px}
.slide-photo{position:absolute;left:7px;top:6px;width:601px;height:204px;background:radial-gradient(ellipse at 45% 45%,#e2e2e2 0%,#b8b8b8 55%,#8f8f8f 100%)}
.slider-dots{position:absolute;left:14px;top:213px;display:flex;gap:2px}
.slider-dots span{width:7px;height:7px;border-radius:50%;background:#c4c4c4}
.slider-dots span.on{background:#8a8a8a}
.slider-arrows{position:absolute;right:13px;top:212px;display:flex;gap:3px}
.slider-arrows span{width:10px;height:10px;border-radius:50%;background:#cfcfcf}
.slider-arrows span+span{background:#8e8e8e}

/* post cards */
.post-card{top:418px;width:145px;height:211px;background:var(--card);border:1px solid var(--card-line);border-radius:4px}
.post-thumb{position:absolute;left:9px;top:9px;width:126px;height:77px}
.post-title{position:absolute;left:10px;width:130px;font-size:11.5px;font-weight:400;line-height:14px;color:var(--ink)}
.post-text{position:absolute;left:10px;top:126px;width:125px;font-family:"Open Sans",sans-serif;font-size:7.5px;line-height:11.5px;color:var(--muted)}
.read-more{position:absolute;left:9px;bottom:9px;font-size:9px;font-weight:600;color:var(--ink-soft);display:flex;align-items:center;gap:4px;line-height:1}
.read-more svg{width:9px;height:9px}

/* popular */
.popular-box{left:146px;top:658px;width:417px;height:181px;background:var(--card);border:1px solid var(--card-line);border-radius:6px}
.pop-item{position:absolute;width:91px}
.pop-thumb{width:91px;height:58px}
.pop-name{font-size:5.5px;font-weight:600;color:#222;margin-top:3px;line-height:7px;white-space:nowrap;overflow:hidden}
.pop-stats{font-size:5px;color:#999;line-height:6px}

/* community */
.community-box{left:577px;top:658px;width:183px;height:185px;background:var(--card);border:1px solid var(--card-line);border-radius:6px}
.community-photo{position:absolute;left:10px;top:8px;width:162px;height:68px;display:flex}
.community-photo div{flex:1}
.community-title{position:absolute;left:12px;top:82px;font-size:11px;color:var(--ink)}
.community-text{position:absolute;left:12px;top:108px;width:160px;font-family:"Open Sans",sans-serif;font-size:8px;line-height:12px;color:var(--muted)}

/* footer */
.footer{left:0;top:853px;width:900px;height:226px;background:repeating-linear-gradient(45deg,#2f2f2f 0 2px,#2a2a2a 2px 4px);border-top:1px solid #4a4a4a}
.footer-heading{position:absolute;font-size:14px;color:#e3e3e3;display:flex;align-items:center;gap:6px;line-height:1}
.footer-list{position:absolute;list-style:none}
.footer-list li{position:relative;padding-left:22px;font-size:9.5px;line-height:13px;color:var(--footer-text)}
.footer-list li svg{position:absolute;left:2px;top:2px;width:10px;height:9px}
.footer-title{position:absolute;font-family:"Oswald",sans-serif;font-weight:600;color:var(--red);line-height:1}
.about-text{position:absolute;left:593px;top:82px;width:154px;text-align:right;font-family:"Open Sans",sans-serif;font-size:8px;line-height:11.2px;color:var(--footer-faint)}
.bottom-bar{left:0;top:1079px;width:900px;height:44px;background:var(--footer-deep);border-top:1px solid #111}
.copyright{position:absolute;left:142px;top:16px;font-size:8.5px;color:#bdbdbd}
.social{position:absolute;left:613px;top:13px;display:flex;gap:6px}
.social span{width:15px;height:15px;border-radius:3px;background:#4d6a8e}
.social span:first-child{border-radius:50%;background:#5aa0c8}
</style>
</head>
<body>
<div class="stage">

  <div class="abs top-pill" style="left:388px;width:99px"><span class="accent">SIGN</span> IN</div>
  <div class="abs top-pill" style="left:493px;width:104px"><span class="accent">REGI</span>STER</div>
  <div class="abs search"><div class="search-field">Search...</div><div class="search-go">Go</div></div>

  <header class="abs masthead">
    <span class="brand-mark"></span>
    <div class="brand-name">GEARLOFTIC</div>
    <div class="brand-tag">mechanical engineering related projects</div>
    <nav class="main-nav">
      <a>Home</a><a class="current">Create</a><a>Tutorials</a><a>Build</a><a>Buy</a>
    </nav>
  </header>

  <div class="abs submit-label">SUBMIT YOUR WORK</div>
  <svg class="abs" style="left:560px;top:108px" width="72" height="40" viewBox="0 0 72 40">
    <path d="M4 36 C14 14 38 6 62 12" fill="none" stroke="#c8321a" stroke-width="4" stroke-linecap="round"/>
    <path d="M56 4 L70 13 L56 20 Z" fill="#c8321a"/>
  </svg>
  <div class="abs make-pill">MAKE</div>

  <section class="abs slider">
    <div class="slide-photo" role="img" aria-label="Rendered model of a twin-cylinder engine with cooling fins and gears"></div>
    <div class="slider-dots"><span></span><span class="on"></span><span></span><span></span></div>
    <div class="slider-arrows"><span></span><span></span></div>
  </section>

  <h2 class="abs heading" style="left:143px;top:398px"><span class="accent">LATEST</span>PROJECTS</h2>
  <h2 class="abs heading" style="left:460px;top:398px"><span class="accent">TUTO</span>RIALS</h2>

  <article class="abs post-card" style="left:144px">
    <div class="post-thumb" role="img" aria-label="Rendered electric motor assembly in red and grey" style="background:linear-gradient(135deg,#3a3a3a,#9a4a3a 50%,#c8c8c8)"></div>
    <h3 class="post-title" style="top:93px">Motor \ motor designed in ShapeForge</h3>
    <p class="post-text">Motor designed in ShapeForge all. This with all parameters, drawn four years</p>
    <div class="read-more"><svg viewBox="0 0 9 9"><path d="M3 0h3v3h3v3H6v3H3V6H0V3h3z" fill="#7cbb1e"/></svg>Read More</div>
  </article>

  <article class="abs post-card" style="left:301px">
    <div class="post-thumb" role="img" aria-label="Model aerobatic plane flying over desert" style="background:linear-gradient(#c98a5a,#b5643a)"></div>
    <h3 class="post-title" style="top:100px">Aerobat 300</h3>
    <p class="post-text">Rc model for engine 26cc<br><br>Rc model for engine 26cc<br>Rc model for engine 26cc</p>
    <div class="read-more"><svg viewBox="0 0 9 9"><path d="M3 0h3v3h3v3H6v3H3V6H0V3h3z" fill="#7cbb1e"/></svg>Read More</div>
  </article>

  <article class="abs post-card" style="left:458px">
    <div class="post-thumb" role="img" aria-label="Sheet metal design workbench screenshot" style="background:linear-gradient(135deg,#1c2a2c,#2f6a6e 50%,#14191a)"></div>
    <h3 class="post-title" style="top:93px">VectaCAD V5 Generative Sheetmetal design</h3>
    <p class="post-text">This four step tutorial shows how to model sheet metal part in VectaCAD generative sheetmetal design workbench.</p>
    <div class="read-more"><svg viewBox="0 0 9 9"><path d="M3 0h3v3h3v3H6v3H3V6H0V3h3z" fill="#7cbb1e"/></svg>Read More</div>
  </article>

  <article class="abs post-card" style="left:615px">
    <div class="post-thumb" role="img" aria-label="CAD window showing a cylinder part" style="background:linear-gradient(#dfe6ee,#f6f6f6 40%,#b9bfc6)"></div>
    <h3 class="post-title" style="top:97px;white-space:nowrap">Save the project in pdf 3d</h3>
    <p class="post-text">gostaria de saber como savar um modelo em um pdf e visualiza-lo em 3d</p>
    <div class="read-more"><svg viewBox="0 0 9 9"><path d="M3 0h3v3h3v3H6v3H3V6H0V3h3z" fill="#7cbb1e"/></svg>Read More</div>
  </article>

  <h2 class="abs heading" style="left:144px;top:640px"><span class="accent">POPULAR</span></h2>
  <section class="abs popular-box">
    <div class="pop-item" style="left:20px;top:12px"><div class="pop-thumb" role="img" aria-label="Brake disc with red caliper" style="background:radial-gradient(circle at 55% 50%,#b62a22,#1a1a1a 60%)"></div><div class="pop-name">Brake disc stoppra</div><div class="pop-stats">♥71 ◉13789</div></div>
    <div class="pop-item" style="left:116px;top:12px"><div class="pop-thumb" role="img" aria-label="Dark sports car" style="background:linear-gradient(#6a5a4a,#2a2a2a)"></div><div class="pop-name">Nt</div><div class="pop-stats">♥140 ◉13468</div></div>
    <div class="pop-item" style="left:213px;top:12px"><div class="pop-thumb" role="img" aria-label="Pistol model with wooden grip" style="background:linear-gradient(135deg,#d8d8d8,#9a9a9a)"></div><div class="pop-name">Holtz 1911 a1 model goverment pistol</div><div class="pop-stats">♥76 ◉13371</div></div>
    <div class="pop-item" style="left:309px;top:12px"><div class="pop-thumb" role="img" aria-label="White unmanned aircraft" style="background:linear-gradient(#eeeeee,#bdbdbd)"></div><div class="pop-name">Kestrel k-1 uav</div><div class="pop-stats">♥80 ◉12264</div></div>
    <div class="pop-item" style="left:20px;top:97px"><div class="pop-thumb" role="img" aria-label="Cutaway planetary gearbox" style="background:linear-gradient(135deg,#5a5a5a,#c47a2a 50%,#e0e0e0)"></div><div class="pop-name">Planetary gearbox</div><div class="pop-stats">♥112 ◉11473</div></div>
    <div class="pop-item" style="left:116px;top:97px"><div class="pop-thumb" role="img" aria-label="Red and black supercar" style="background:linear-gradient(#f2f2f2,#b23030 55%,#2a2a2a)"></div><div class="pop-name">Vantoro vela</div><div class="pop-stats">♥180 ◉10884</div></div>
    <div class="pop-item" style="left:213px;top:97px"><div class="pop-thumb" role="img" aria-label="V-twin engine render" style="background:radial-gradient(circle,#cfcfcf,#3a3a3a 75%)"></div><div class="pop-name">Tobin's new project phase-1</div><div class="pop-stats">♥141 ◉10240</div></div>
    <div class="pop-item" style="left:309px;top:97px"><div class="pop-thumb" role="img" aria-label="Red sports car" style="background:linear-gradient(#e4e4e4,#d8452a 60%,#bdbdbd)"></div><div class="pop-name">Rossario r458</div><div class="pop-stats">♥89 ◉10001</div></div>
  </section>

  <h2 class="abs heading" style="left:580px;top:640px"><span class="accent">COMM</span>UNITY</h2>
  <section class="abs community-box">
    <div class="community-photo">
      <div role="img" aria-label="Member working on an illuminated circuit board" style="background:linear-gradient(#8a3a2a,#1e2a5a 50%,#2b3a8a)"></div>
      <div role="img" aria-label="Wire-frame walking machine sculpture" style="background:linear-gradient(#9a9ab8,#6e6e8c)"></div>
    </div>
    <div class="community-title">Member of the month</div>
    <p class="community-text">Weeks later of googling, and reading forum after forum I came up with a circuit that I was happy with. Realistically this would have been easie....</p>
    <div class="read-more" style="left:11px;bottom:8px"><svg viewBox="0 0 9 9"><path d="M3 0h3v3h3v3H6v3H3V6H0V3h3z" fill="#7cbb1e"/></svg>Read More</div>
  </section>

  <footer class="abs footer">
    <div class="footer-heading" style="left:142px;top:28px">
      <svg width="17" height="17" viewBox="0 0 17 17"><rect x="1" y="1" width="14" height="15" fill="#f2f2f2"/><path d="M4 6h8M4 9h8M4 12h6" stroke="#999" stroke-width="1"/><path d="M12 1l4 3-6 8-2 1 0-2z" fill="#e0a23a"/></svg>
      Recent Posts
    </div>
    <ul class="footer-list" style="left:143px;top:60px;width:190px">
      <li style="margin-bottom:11px"><svg viewBox="0 0 10 9"><path d="M1 5l3 3 5-7" fill="none" stroke="#7cbb1e" stroke-width="2"/></svg>Tutorial: ShapeForge Mold Tools</li>
      <li style="margin-bottom:14px"><svg viewBox="0 0 10 9"><path d="M1 5l3 3 5-7" fill="none" stroke="#7cbb1e" stroke-width="2"/></svg>How to model Aurel R8 using sketch tracer in VectaCAD v5?</li>
      <li style="margin-bottom:13px"><svg viewBox="0 0 10 9"><path d="M1 5l3 3 5-7" fill="none" stroke="#7cbb1e" stroke-width="2"/></svg>Video Tutorial on Modeling &amp; Simulating CAM Follower Mechanism</li>
      <li style="margin-bottom:11px"><svg viewBox="0 0 10 9"><path d="M1 5l3 3 5-7" fill="none" stroke="#7cbb1e" stroke-width="2"/></svg>Taking the key way measurement in</li>
      <li><svg viewBox="0 0 10 9"><path d="M1 5l3 3 5-7" fill="none" stroke="#7cbb1e" stroke-width="2"/></svg>Is it possible to mirror a variable radius fillet in ShapeForge?</li>
    </ul>

    <div class="footer-heading" style="left:360px;top:28px">
      <svg width="18" height="18" viewBox="0 0 18 18"><rect x="1" y="2" width="16" height="15" rx="1" fill="#f2f2f2"/><rect x="1" y="2" width="16" height="5" fill="#e07a2a"/><text x="9" y="15" font-size="7" text-anchor="middle" fill="#333" font-family="Source Sans 3,sans-serif">15</text></svg>
      Archives
    </div>
    <ul class="footer-list" style="left:362px;top:60px;width:150px">
      <li style="margin-bottom:10px"><svg viewBox="0 0 10 9"><path d="M1 5l3 3 5-7" fill="none" stroke="#7cbb1e" stroke-width="2"/></svg>January 2013</li>
      <li style="margin-bottom:10px"><svg viewBox="0 0 10 9"><path d="M1 5l3 3 5-7" fill="none" stroke="#7cbb1e" stroke-width="2"/></svg>February 2013</li>
      <li style="margin-bottom:10px"><svg viewBox="0 0 10 9"><path d="M1 5l3 3 5-7" fill="none" stroke="#7cbb1e" stroke-width="2"/></svg>March 2013</li>
      <li style="margin-bottom:10px"><svg viewBox="0 0 10 9"><path d="M1 5l3 3 5-7" fill="none" stroke="#7cbb1e" stroke-width="2"/></svg>April 2013</li>
      <li style="margin-bottom:10px"><svg viewBox="0 0 10 9"><path d="M1 5l3 3 5-7" fill="none" stroke="#7cbb1e" stroke-width="2"/></svg>May 2013</li>
      <li><svg viewBox="0 0 10 9"><path d="M1 5l3 3 5-7" fill="none" stroke="#7cbb1e" stroke-width="2"/></svg>June 2013</li>
    </ul>

    <div class="footer-title" style="left:651px;top:25px;font-size:21px">ABOUT US</div>
    <p class="about-text">Lorem ipsum dolor sit amet, consectetur adipisicing elit, sed do eiusmod tempor incididunt ut or in aecat cupidatat non proident, sunt in culpa qui officia deserunt mollit anim id est laborum.</p>
    <div class="footer-title" style="left:668px;top:176px;font-size:15px">CONTACT US</div>
  </footer>

  <div class="abs bottom-bar">
    <div class="copyright">© Copyright 2013 Gearloftic All Right Reserved</div>
    <div class="social" aria-label="Social links"><span></span><span></span><span></span></div>
  </div>

</div>
</body>
</html>
```